Business card with logo for a family psychologist

I need a business card for my private practice in the urban Chicago area as a psychologist. I see families and individuals who are going through difficult times - divorce, separation, illness, or trauma. I want to project hopefulness, competence, and caring.

Target Market(s)

Adults, other professionals - such as physicans and lawyers

Industry/Entity Type

Health Care

Contact Information for Business Card

Front should have my name and credentials; back should have location information including my email, phone

Font styles to use
Serif
Decorative
Script

Requirements
Must have
• Unique logo
Should not have
• No pictures or icons of people; no black

```html
<!DOCTYPE html>
<html lang="en">
<head>
<meta charset="utf-8">
<title>Business Card — Licensed Clinical Psychologist</title>
<link rel="stylesheet" href="https://fonts.googleapis.com/css2?family=Alegreya:wght@400;500;700&display=swap">
<style>
  :root {
    --green: #7cc142;
    --green-light: #a6d23c;
    --pink: #ee5aa0;
    --ink: #444444;
    --card: #ffffff;
    --backdrop: #efe8de;
  }
  * { box-sizing: border-box; margin: 0; padding: 0; }
  html, body {
    width: 1200px; height: 1076px; overflow: hidden;
    background: var(--backdrop);
    font-family: "Alegreya", Georgia, serif;
  }
  .card {
    position: absolute; left: 190px;
    width: 820px; height: 470px;
    background: var(--card);
    border-radius: 22px;
    box-shadow: 0 6px 18px rgba(90, 70, 40, 0.22);
    overflow: hidden;
  }
  .card--front { top: 45px; }
  .card--back { top: 561px; }
  .rule {
    position: absolute; left: 0; width: 100%; height: 4px;
    background: var(--pink);
  }
  .rule--top { top: 52px; }
  .rule--bottom { top: 244px; }
  .band {
    position: absolute; left: 0; top: 62px; width: 100%; height: 177px;
    background: linear-gradient(90deg, var(--green) 0%, var(--green-light) 45%, var(--green-light) 55%, var(--green) 100%);
  }
  .brand {
    position: absolute; left: 290px; top: 30px;
    width: 240px; height: 240px; border-radius: 50%;
    background: var(--card);
    display: flex; flex-direction: column; align-items: center; justify-content: center;
    color: var(--green); font-weight: 500; font-size: 27px; line-height: 1.15; text-align: center;
  }
  .title {
    position: absolute; left: 0; top: 262px; width: 100%;
    text-align: center; color: var(--green);
  }
  .title__main { font-size: 48px; font-weight: 500; line-height: 1; }
  .title__sub {
    display: flex; align-items: center; justify-content: center; gap: 12px;
    font-size: 36px; line-height: 1.1;
  }
  .title__sub::before, .title__sub::after {
    content: ""; width: 76px; height: 2px; background: var(--pink);
  }
  .person {
    position: absolute; left: 0; top: 372px; width: 100%;
    text-align: center; color: var(--ink);
    font-size: 32px; font-weight: 500;
  }
  .contact {
    position: absolute; left: 0; top: 372px; width: 100%;
    text-align: center; color: var(--ink); font-size: 21px; line-height: 1.6;
  }
  .contact__label { color: var(--pink); }
</style>
</head>
<body>
  <section class="card card--front">
    <div class="rule rule--top"></div>
    <div class="band"></div>
    <div class="rule rule--bottom"></div>
    <div class="brand"><span>Brightwater</span><span>Family Practice</span></div>
    <div class="title">
      <div class="title__main">Licensed Clinical</div>
      <div class="title__sub">Psychologist</div>
    </div>
    <p class="person">Dana Whitfield, Ph.D.</p>
  </section>

  <section class="card card--back">
    <div class="rule rule--top"></div>
    <div class="band"></div>
    <div class="rule rule--bottom"></div>
    <div class="brand"><span>Brightwater</span><span>Family Practice</span></div>
    <div class="title">
      <div class="title__main">Licensed Clinical</div>
      <div class="title__sub">Psychologist</div>
    </div>
    <div class="contact">
      <p><span class="contact__label">Phone:</span> 312-555-0148 | <span class="contact__label">Email:</span> hello@whitfieldpsych.com</p>
      <p>240 W. Lakeview Ave Suite 310, Chicago, Illinois 60614</p>
    </div>
  </section>
</body>
</html>
```